New Solo Law Office Needs Business Card/Letterhead Design

I am starting a solo law office called "Law Office of Brian Kolmer, PLLC" in Tucson, Arizona. I will be doing criminal defense trial work. More than a logo with any sort of icon, I am really just looking for the name of the company to be displayed in a sleek, minimalist but interesting sort of way, with a format and font type that communicates professionalism. It can be in color, but doesn't have to be, and I am thinking blue and/or red accents colors. I'd like it to convey that I am passionate, dependable and willing to fight. For the business card, I envision sort of higher quality card material, and maybe some embossing or raised print. I will want to include my company name, name, phone and fax numbers, email and website addresses. For the letterhead, I will want to be able to use the same sort of font/formatting design as on the business card.
Industry/Entity Type
Business
Contact Information for Business Card
Law Office of Brian Kolmer, PLLC
Brian Kolmer
brian@kolmer-law.example
www.kolmer-law.example
(I do not yet have an established phone or fax number, so please put in some place holder numbers for the formatting, and I can add the actual numbers in before I print.)
Colors
Designer to choose colors to be used in the design.
Look and feel
Each slider illustrates characteristics of the customer's brand and the style your logo design should communicate.

```html
<!DOCTYPE html>
<html lang="en">
<head>
<meta charset="utf-8">
<title>Law Office of Brian Kolmer, PLLC – Business Card</title>
<link rel="stylesheet" href="https://fonts.googleapis.com/css2?family=Arimo:wght@400;700&display=swap">
<style>
  :root {
    --bg: #e6e7e9;
    --card: #f6f6f6;
    --brand-blue: #1a86cc;
    --ink: #111111;
    --ink-soft: #333333;
    --white: #ffffff;
  }
  * { box-sizing: border-box; margin: 0; padding: 0; }
  html, body {
    width: 1200px; height: 1000px; overflow: hidden;
    background: var(--bg);
    font-family: "Arimo", Arial, sans-serif;
  }
  .business-card {
    position: absolute; left: 140px; top: 237px;
    width: 920px; height: 526px;
    background: var(--card);
    border-radius: 18px;
    box-shadow: 0 10px 30px rgba(0,0,0,.18);
    overflow: hidden;
  }
  .firm-mark {
    position: absolute; left: 210px; top: 100px;
    display: flex; align-items: center; gap: 18px;
  }
  .firm-mark__square {
    width: 64px; height: 64px; background: var(--brand-blue);
  }
  .firm-mark__name {
    font-size: 26px; font-weight: 400; color: var(--ink);
    text-transform: uppercase; letter-spacing: .5px; line-height: 1.1;
    max-width: 420px;
  }
  .attorney {
    position: absolute; left: 0; right: 0; top: 200px; text-align: center;
  }
  .attorney__name { font-size: 26px; font-weight: 700; color: var(--ink); }
  .attorney__title { font-size: 17px; color: var(--ink-soft); margin-top: 4px; }
  .contact-band {
    position: absolute; left: 0; right: 0; top: 310px; height: 96px;
    background: var(--brand-blue);
  }
  .contact-item {
    position: absolute; top: -22px; width: 300px;
    display: flex; flex-direction: column; align-items: center; gap: 14px;
  }
  .contact-item--phone { left: 10px; }
  .contact-item--email { left: 310px; }
  .contact-item--web { left: 610px; }
  .contact-item__icon {
    width: 44px; height: 44px; border-radius: 50%;
    background: var(--white); border: 3px solid var(--brand-blue);
    display: flex; align-items: center; justify-content: center;
  }
  .contact-item__text { font-size: 21px; font-weight: 700; color: var(--white); white-space: nowrap; }
  .address {
    position: absolute; left: 0; right: 0; top: 436px;
    text-align: center; font-size: 22px; color: var(--ink);
  }
</style>
</head>
<body>
  <article class="business-card">
    <header class="firm-mark">
      <div class="firm-mark__square"></div>
      <div class="firm-mark__name">Law Office of<br>Brian Kolmer, PLLC</div>
    </header>

    <section class="attorney">
      <div class="attorney__name">Brian Kolmer</div>
      <div class="attorney__title">Criminal Defense Lawyer</div>
    </section>

    <section class="contact-band">
      <div class="contact-item contact-item--phone">
        <span class="contact-item__icon">
          <svg width="22" height="22" viewBox="0 0 24 24" aria-hidden="true">
            <path fill="#1a86cc" d="M6.6 10.8a15 15 0 0 0 6.6 6.6l2.2-2.2c.3-.3.7-.4 1-.2 1.1.4 2.3.6 3.6.6.6 0 1 .4 1 1V20c0 .6-.4 1-1 1A17 17 0 0 1 3 4c0-.6.4-1 1-1h3.5c.6 0 1 .4 1 1 0 1.3.2 2.5.6 3.6.1.3 0 .7-.2 1z"/>
          </svg>
        </span>
        <span class="contact-item__text">000 0000 0000</span>
      </div>
      <div class="contact-item contact-item--email">
        <span class="contact-item__icon">
          <svg width="22" height="22" viewBox="0 0 24 24" aria-hidden="true">
            <rect x="3" y="6" width="18" height="12" fill="none" stroke="#1a86cc" stroke-width="2"/>
            <path d="M3 6l9 7 9-7" fill="none" stroke="#1a86cc" stroke-width="2"/>
          </svg>
        </span>
        <span class="contact-item__text">brian@kolmer-law.example</span>
      </div>
      <div class="contact-item contact-item--web">
        <span class="contact-item__icon">
          <svg width="22" height="22" viewBox="0 0 24 24" aria-hidden="true">
            <g fill="none" stroke="#1a86cc" stroke-width="1.8">
              <circle cx="12" cy="12" r="9"/>
              <ellipse cx="12" cy="12" rx="4" ry="9"/>
              <path d="M3 12h18M5 7h14M5 17h14"/>
            </g>
          </svg>
        </span>
        <span class="contact-item__text">www.kolmer-law.example</span>
      </div>
    </section>

    <p class="address">Your Street Address Here, Sample City, ST 00000</p>
  </article>
</body>
</html>
```